Brimwork sales

🎨 Project Title:
Brimwork Designer Web Page for WooCommerce (French Texts Provided) i show you exemple what i need

📄 Project Description:
We are looking to create a web page design (desktop and mobile) for a custom cap ordering experience. This page will be integrated into our existing WooCommerce transactional site. The goal is to allow customers to configure and order personalized caps easily and visually.

The entire interface will ultimately be in French, but you can design using placeholder texts (we will provide the actual French text later).

💡 Page Goals & Features:
The page should be modern, clean, and conversion-oriented, and include the following features:

Header area:

Visually showcase examples of designed caps (carousel or grid layout)

A clear title and short description

Customization Steps (in order):

Material selection: users choose the type of material for the cap

Cap color: users choose the base color of the cap

Patch shape: users select the shape of the patch (e.g., round, square, rectangle, custom)

Patch location: mainly the front, but possibly add other options

Quantity selection: users choose how many units they want (with price updates)

Price display: show price per unit and total cost depending on quantity

Call to Action (CTA):

Add to cart or request a quote button

Smooth integration with WooCommerce logic (cart, checkout, etc.)

Other Optional Sections:

FAQ

Delivery timeline

Client testimonials or reviews

🛠 Technical Notes:
The design must be compatible with WooCommerce

Responsive design for both desktop and mobile

The final output can be delivered in Figma, Adobe XD, or layered PSD (no coding required for now)

We will handle the French translation; just use placeholder text where needed

🖼 Inspiration / Style:
Clean and modern layout

Easy to navigate

Visual configurator-style approach (like t-shirt or shoe customization sites)

Feel free to use mockups of caps to enhance the presentation

📎 What we will provide:
Actual French text

Product images (caps, patch styles, color swatches)

Brand logo and colors

Optional references if needed

✅ Deliverables:
Homepage (or dedicated product page) layout

Mobile and desktop views

Editable design file (Figma, XD, PSD)

i need very nice 1 or 2 hat design to present to customer design un der the hat and front and see coupple of shape of the patche to show option possible

```html
<!DOCTYPE html>
<html lang="en">
<head>
<meta charset="utf-8">
<title>Brimwork – Custom Hat Designer</title>
<link href="https://fonts.googleapis.com/css2?family=Playfair+Display:ital,wght@0,700;0,800;1,600&family=Lato:wght@400;700&display=swap" rel="stylesheet">
<style>
:root{
  --orange:#ff6b22;
  --orange-soft:#ffa07a;
  --peach:#fde6dc;
  --peach-deep:#f6cdb8;
  --ink:#111111;
  --text:#2b2b2b;
  --muted:#5a5a5a;
  --line:#d9d9d9;
  --white:#ffffff;
  --footer:#000000;
}
*{box-sizing:border-box;margin:0;padding:0}
html,body{width:1200px;height:3454px;overflow:hidden}
body{font-family:'Lato',sans-serif;color:var(--text);background:var(--white);position:relative}
.abs{position:absolute}
.serif{font-family:'Playfair Display',serif}
.accent{color:var(--orange)}

/* top bar */
.topbar{left:0;top:0;width:1200px;height:32px;background:var(--orange);color:var(--white);font-size:13px}
.topbar span{position:absolute;top:8px}
.topbar .sep{position:absolute;top:0;width:1px;height:32px;background:rgba(255,255,255,.6)}

/* header */
.brand{font-family:'Playfair Display',serif;font-weight:700;font-size:27px;color:var(--ink)}
.search{left:324px;top:59px;width:458px;height:42px;border:1px solid #bdbdbd;border-radius:22px;font-size:15px;color:var(--muted)}
.search .cat{position:absolute;left:0;top:0;width:175px;height:40px;border-right:1px solid #bdbdbd;background:#f3f3f3;border-radius:22px 0 0 22px;padding:10px 22px;color:#333}
.search .q{position:absolute;left:216px;top:11px}
.cart{left:968px;top:56px;width:120px;height:42px;border:1px solid #bdbdbd;border-radius:22px;background:#f0f0f0;font-size:15px;color:#555;padding:11px 0 0 46px}
.nav{top:132px;font-size:15px;color:var(--ink)}
.nav a{color:inherit;text-decoration:none;position:absolute;white-space:nowrap}

/* hero */
.hero{left:0;top:172px;width:1200px;height:461px;background:linear-gradient(100deg,#f7dccd 0%,#fbe6da 45%,#f3c9b3 100%)}
.hero-photo{position:absolute;right:0;top:0;width:430px;height:461px;background:linear-gradient(160deg,#e9b58f 0%,#d9a07c 40%,#c9a6b4 100%)}
.hero h1{position:absolute;left:108px;top:88px;font-family:'Playfair Display',serif;font-weight:800;font-size:55px;line-height:66px;color:var(--ink)}
.hero h1 em{font-style:italic;font-weight:600}
.hero p{position:absolute;left:110px;top:240px;font-size:15px;color:#333}
.btn{display:flex;align-items:center;justify-content:center;gap:12px;background:var(--orange);color:var(--white);font-weight:700;font-size:18px;border-radius:4px}
.hero .btn{position:absolute;left:110px;top:292px;width:177px;height:47px}

.section-title{left:0;width:1200px;text-align:center;font-family:'Playfair Display',serif;font-weight:700;font-size:46px;color:var(--ink)}

/* configurator */
.config{left:110px;top:800px;width:979px;height:615px;background:var(--peach);border-radius:6px;box-shadow:0 2px 8px rgba(0,0,0,.15)}
.product-photo{position:absolute;left:18px;top:130px;width:410px;height:320px;border-radius:50%/45%;background:radial-gradient(ellipse at 50% 55%,#e6d4a8 0%,#d9c289 55%,#7aa5c0 80%,var(--peach) 100%)}
.divider{position:absolute;left:489px;top:17px;width:1px;height:558px;background:#222}
.p{position:absolute;left:532px}
.p-title{top:22px;font-family:'Playfair Display',serif;font-weight:700;font-size:42px;color:var(--ink)}
.stars{color:#f7c51c;letter-spacing:2px}
.opt{position:absolute;left:526px;width:326px;background:var(--white);border-radius:4px;box-shadow:0 1px 4px rgba(0,0,0,.08);padding:10px 16px;font-size:14px;color:#222}
.opt small{font-size:12px}
.swatches{display:flex;gap:8px;align-items:center;margin-top:10px}
.sw{width:21px;height:21px;border-radius:50%}
.field{border:1px solid #999;border-radius:3px;background:var(--white);font-size:15px;display:flex;align-items:center;justify-content:center}
.btn-outline{border:2px solid var(--orange);border-radius:4px;background:var(--white);color:var(--orange);font-size:17px;display:flex;align-items:center}

.arrow{width:25px;height:25px;border-radius:50%;display:flex;align-items:center;justify-content:center}
.arrow.dark{background:var(--ink)}
.arrow.grey{background:#5f5f5f}

/* faq */
.faq{left:0;top:1498px;width:1200px;height:675px;background:linear-gradient(100deg,#c9a77a 0%,#e5d2bb 28%,#dfe3e3 55%,#e7cdb6 100%)}
.faq h2{position:absolute;left:0;top:72px;width:1200px;text-align:center;font-family:'Playfair Display',serif;font-weight:700;font-size:46px;color:var(--ink)}
.faq-item{position:absolute;left:642px;width:446px;background:var(--white);border:1px solid #e0e0e0;font-size:15px;color:#222;padding:0 24px}
.faq-item .q{height:45px;line-height:45px}
.faq-item.open{border-color:var(--orange)}
.faq-item.open .q{border-bottom:1px solid var(--orange);margin:0 -24px;padding:0 24px}
.faq-item .a{font-size:14px;line-height:26px;color:#444;padding:14px 0 12px 3px}

/* testimonials */
.tcard{top:2337px;width:473px;height:185px;background:var(--peach);border-radius:8px;box-shadow:0 2px 6px rgba(0,0,0,.18)}
.avatar{position:absolute;left:14px;top:20px;width:80px;height:80px;border-radius:50%}
.tname{position:absolute;left:114px;top:34px;font-size:18px;color:var(--ink)}
.tcity{position:absolute;left:114px;top:58px;font-size:17px;color:var(--orange)}
.tstars{position:absolute;left:112px;top:84px;font-size:12px}
.tquote{position:absolute;right:44px;top:20px;font-family:'Playfair Display',serif;font-size:40px;color:var(--orange);line-height:1}
.ttext{position:absolute;left:16px;top:126px;width:445px;font-size:13px;line-height:24px;color:#444}

/* delivery */
.step{top:2773px;width:360px;text-align:center}
.step .circle{margin:0 auto;width:148px;height:148px;border-radius:50%;background:var(--white);box-shadow:0 3px 14px rgba(0,0,0,.15);display:flex;align-items:center;justify-content:center}
.step h3{margin-top:22px;font-size:24px;font-weight:400;color:var(--ink)}
.step p{margin-top:8px;font-size:15px;line-height:23px;color:#444}

/* footer */
.footer{left:0;top:3102px;width:1200px;height:352px;background:var(--footer);color:var(--white)}
.footer h4{position:absolute;top:82px;font-family:'Playfair Display',serif;font-weight:700;font-size:22px;color:var(--orange)}
.flist{position:absolute;top:124px;list-style:none;font-size:16px}
.flist li{height:34px;display:flex;align-items:center;gap:14px}
.flist li::before{content:"";width:8px;height:8px;background:var(--orange)}
.contact{position:absolute;left:868px;font-size:16px;display:flex;gap:14px;line-height:25px}
.contact .ic{width:21px;height:21px;border-radius:50%;background:var(--orange);flex:none;margin-top:2px;display:flex;align-items:center;justify-content:center}
.newsletter{position:absolute;left:110px;top:188px;width:270px;height:50px;background:var(--white);border-radius:4px;color:#444;font-size:14px}
.newsletter span{position:absolute;left:16px;top:16px}
.newsletter b{position:absolute;right:0;top:0;width:92px;height:50px;background:var(--orange);border-radius:4px;color:var(--white);font-weight:400;font-size:19px;display:flex;align-items:center;justify-content:center}
.social{position:absolute;top:263px;width:21px;height:21px;border-radius:50%}
.copy{position:absolute;left:110px;top:313px;width:979px;border-top:1px solid #333;padding-top:10px;text-align:center;font-size:12px}
</style>
</head>
<body>

<!-- Top bar -->
<div class="abs topbar">
  <span style="left:110px">Free Delivery</span>
  <div class="sep" style="left:221px"></div>
  <span style="left:249px">Free Returns</span>
  <span style="left:866px">My Account</span>
  <div class="sep" style="left:960px"></div>
  <span style="left:984px;width:20px;height:13px;background:#1f3a8a;border:1px solid #fff"></span>
  <span style="left:1015px">English</span>
  <svg class="abs" style="left:1066px;top:10px" width="14" height="10" viewBox="0 0 14 10"><path d="M1 2l6 6 6-6" stroke="#fff" stroke-width="2" fill="none"/></svg>
</div>

<!-- Header -->
<div class="abs" style="left:110px;top:50px;width:36px;height:36px;border-radius:50%;background:var(--ink)"></div>
<div class="abs brand" style="left:156px;top:48px">Brim<span class="accent">work</span></div>

<div class="abs search">
  <div class="cat">All Categories
    <svg style="position:absolute;right:24px;top:15px" width="14" height="9" viewBox="0 0 14 9"><path d="M1 1l6 6 6-6" stroke="#333" stroke-width="2" fill="none"/></svg>
  </div>
  <span class="q">Search Here...</span>
  <svg style="position:absolute;right:16px;top:10px" width="20" height="20" viewBox="0 0 20 20"><circle cx="8.5" cy="8.5" r="6.5" stroke="#777" stroke-width="1.6" fill="none"/><path d="M13.5 13.5l5 5" stroke="#777" stroke-width="1.6"/></svg>
</div>
<div class="abs" style="left:837px;top:66px;font-size:15px;color:#555">Login &nbsp;<span style="font-size:20px">/</span>&nbsp; Register</div>
<div class="abs cart">
  <svg style="position:absolute;left:16px;top:12px" width="18" height="16" viewBox="0 0 18 16"><path d="M1 5h16l-2 10H3z" stroke="#777" stroke-width="1.5" fill="none"/><path d="M5 5V3h8v2" stroke="#777" stroke-width="1.5" fill="none"/></svg>
  4 item(s)
</div>

<nav class="abs nav" style="left:0;width:1200px">
  <a href="#" style="left:110px;color:var(--orange);text-decoration:underline">Home</a>
  <a href="#" style="left:190px">Customization Hat</a>
  <a href="#" style="left:355px">FAQ</a>
  <a href="#" style="left:424px">Delivery &nbsp;timeline</a>
  <a href="#" style="left:581px">Testimonials</a>
  <a href="#" style="left:936px">Call : +1 555 014 2290</a>
</nav>

<!-- Hero -->
<section class="abs hero">
  <div class="hero-photo" role="img" aria-label="Smiling woman wearing a straw sun hat"></div>
  <h1>Built with <span class="accent">Precision</span><br><em>Designed by <span class="accent">You.</span></em></h1>
  <p>Start customizing your cap: premium materials, bold styles, and expert detail.</p>
  <a class="btn" href="#">Get Started
    <svg width="34" height="20" viewBox="0 0 34 20"><path d="M6 14c0-7 5-12 11-12s11 5 11 12" fill="#fff"/><path d="M1 15c8 4 24 4 32 0" stroke="#fff" stroke-width="3" fill="none"/></svg>
  </a>
</section>

<!-- Configurator -->
<h2 class="abs section-title" style="top:696px">Customiz <span class="accent">Hat</span></h2>

<div class="abs arrow dark" style="left:43px;top:1101px"><svg width="10" height="12" viewBox="0 0 10 12"><path d="M8 1L2 6l6 5" stroke="#fff" stroke-width="2.4" fill="none"/></svg></div>
<div class="abs arrow grey" style="left:1132px;top:1101px"><svg width="10" height="12" viewBox="0 0 10 12"><path d="M2 1l6 5-6 5" stroke="#fff" stroke-width="2.4" fill="none"/></svg></div>

<section class="abs config">
  <div class="product-photo" role="img" aria-label="Straw sun hat with a blue patterned brim and a front logo patch"></div>
  <div class="divider"></div>

  <div class="p p-title">Mat Straw</div>
  <div class="p stars" style="top:80px;font-size:24px">★★★★★</div>
  <div class="p" style="top:124px;font-size:24px;color:var(--ink)">$70.00</div>
  <div class="p" style="left:624px;top:133px;font-size:14px;color:#555;text-decoration:line-through">$80.00</div>
  <div class="p" style="left:692px;top:125px;width:86px;height:33px;border-radius:17px;background:var(--orange);color:#fff;font-size:12px;display:flex;align-items:center;justify-content:center">SAVE12%</div>

  <div class="opt" style="top:168px;height:71px">Color: <small>Blue</small>
    <div class="swatches">
      <span class="sw" style="background:#6aa9c0;box-shadow:0 0 0 2px #fff,0 0 0 3px #555"></span>
      <span class="sw" style="background:#f7a98a"></span>
      <span class="sw" style="background:#f48b8b"></span>
      <span class="sw" style="background:#e3e38a"></span>
      <span class="sw" style="background:#7cc46a"></span>
      <span class="sw" style="background:#9a96dd"></span>
      <span class="sw" style="background:#5a6fb0"></span>
      <span style="margin-left:10px;font-size:15px">More..</span>
    </div>
  </div>

  <div class="opt" style="top:254px;height:71px">Patch shape: <small>Round</small>
    <div class="swatches" style="margin-top:14px">
      <span class="sw" style="background:var(--orange-soft)"></span>
      <span style="width:18px;height:18px;background:var(--orange-soft);margin-left:2px"></span>
      <span style="width:27px;height:18px;background:var(--orange-soft);margin-left:4px"></span>
      <span style="margin-left:14px;font-size:13px">custom</span>
    </div>
  </div>

  <div class="p" style="top:337px;font-size:15px">Quantity</div>
  <div class="p field" style="top:368px;width:75px;height:35px;justify-content:space-around">
    <span>−</span><span>1</span><span>+</span>
  </div>
  <div class="p" style="top:414px;font-size:15px">Price</div>
  <div class="p field" style="top:446px;width:75px;height:35px">2</div>
  <div class="p field" style="left:625px;top:446px;width:71px;height:35px">$120.00</div>

  <a class="p btn" href="#" style="top:509px;width:177px;height:47px">Add to cart
    <svg width="34" height="20" viewBox="0 0 34 20"><path d="M6 14c0-7 5-12 11-12s11 5 11 12" fill="#fff"/><path d="M1 15c8 4 24 4 32 0" stroke="#fff" stroke-width="3" fill="none"/></svg>
  </a>
  <a class="p btn-outline" href="#" style="left:724px;top:509px;width:212px;height:47px;padding-left:18px">Request a Quote
    <span style="position:absolute;right:-2px;top:-2px;width:42px;height:47px;background:var(--ink);border-radius:0 4px 4px 0;display:flex;align-items:center;justify-content:center">
      <svg width="22" height="16" viewBox="0 0 22 16"><path d="M2 2l6 6-6 6M11 2l6 6-6 6" stroke="#fff" stroke-width="3" fill="none"/></svg>
    </span>
  </a>
  <div class="p" style="left:770px;top:563px;font-size:14px;font-style:italic">For Bulk Order</div>
</section>

<!-- FAQ -->
<section class="abs faq" role="img" aria-label="Close-up of a hand holding the brim of a straw hat against a soft sky">
  <h2>Frequently Asked <span class="accent">Questions</span></h2>
  <div class="faq-item open" style="top:162px">
    <div class="q">1. How do I customize my cap?</div>
    <div class="a">You can personalize your cap in just a few steps: choose the material, base color, patch shape and location, and the quantity you need. You'll see a live preview as you go.</div>
  </div>
  <div class="faq-item" style="top:330px"><div class="q">2. Can I upload my own design or logo?</div></div>
  <div class="faq-item" style="top:392px"><div class="q">3. What is the minimum order quantity?</div></div>
  <div class="faq-item" style="top:455px"><div class="q">4. How long does production take?</div></div>
  <div class="faq-item" style="top:517px"><div class="q">5. How much does it cost?</div></div>
</section>

<!-- Testimonials -->
<h2 class="abs section-title" style="top:2243px">Testimonials</h2>

<div class="abs arrow dark" style="left:43px;top:2415px"><svg width="10" height="12" viewBox="0 0 10 12"><path d="M8 1L2 6l6 5" stroke="#fff" stroke-width="2.4" fill="none"/></svg></div>
<div class="abs arrow grey" style="left:1132px;top:2415px"><svg width="10" height="12" viewBox="0 0 10 12"><path d="M2 1l6 5-6 5" stroke="#fff" stroke-width="2.4" fill="none"/></svg></div>

<article class="abs tcard" style="left:110px">
  <div class="avatar" role="img" aria-label="Customer portrait" style="background:linear-gradient(160deg,#cfc6bb,#9c8a78)"></div>
  <div class="tname">Lucas R.</div>
  <div class="tcity">Lyon</div>
  <div class="tstars stars">★★★★★</div>
  <div class="tquote">”</div>
  <p class="ttext">The caps looked amazing and the quality was even better than expected. Super smooth ordering process!”</p>
</article>
<article class="abs tcard" style="left:614px">
  <div class="avatar" role="img" aria-label="Customer portrait" style="background:linear-gradient(160deg,#6e7d5c,#3d4a3a)"></div>
  <div class="tname">Amélie D.</div>
  <div class="tcity">Bordeaux</div>
  <div class="tstars stars">★★★★★</div>
  <div class="tquote">”</div>
  <p class="ttext">We ordered 50 custom caps for our company event. Everyone loved them — great material and fast shipping.”</p>
</article>

<!-- Delivery timeline -->
<h2 class="abs section-title" style="top:2676px">Delivery <span class="accent">Timeline</span></h2>

<svg class="abs" style="left:300px;top:2790px" width="600" height="130" viewBox="0 0 600 130">
  <path d="M15 90 C120 140 200 120 245 100" stroke="#111" stroke-width="2.5" stroke-dasharray="10 7" fill="none"/>
  <path d="M370 40 C450 10 530 10 585 40" stroke="#111" stroke-width="2.5" stroke-dasharray="10 7" fill="none"/>
</svg>

<div class="abs step" style="left:63px">
  <div class="circle">
    <svg width="86" height="74" viewBox="0 0 86 74" fill="none" stroke="#e2622a" stroke-width="3"><path d="M14 52C14 26 26 10 43 10s29 16 29 42"/><path d="M4 56c20 10 58 10 78 0v8c-20 8-58 8-78 0z"/><circle cx="43" cy="7" r="3"/><path d="M32 32v-4h4M54 28h4v4M32 40v4h4M58 40v4h-4"/></svg>
  </div>
  <h3>Customization</h3>
  <p>You design it Create your cap with our<br>easy-to-use configurator. Upload your<br>logo and choose your style.</p>
</div>
<div class="abs step" style="left:418px">
  <div class="circle">
    <svg width="80" height="66" viewBox="0 0 80 66" fill="none" stroke="#e2622a" stroke-width="3"><rect x="3" y="3" width="74" height="60" rx="5"/><path d="M3 15h74"/><circle cx="11" cy="9" r="1.5"/><circle cx="18" cy="9" r="1.5"/><circle cx="25" cy="9" r="1.5"/><path d="M12 54V38h8l6-10h4v10h8v16z"/><circle cx="58" cy="30" r="7"/><path d="M47 44h22M47 52h22"/></svg>
  </div>
  <h3>Design Approval</h3>
  <p>We'll craft your first set of cap mockups<br>based on your brief, brand assets, and<br>style preferences. Expect 2–3 high-quality</p>
</div>
<div class="abs step" style="left:773px">
  <div class="circle">
    <svg width="74" height="70" viewBox="0 0 74 70" fill="none" stroke="#e2622a" stroke-width="3"><path d="M10 26l27-14 27 14v30L37 68 10 56z"/><path d="M10 26l27 14 27-14M37 40v28"/><path d="M23 19l27 14v10"/></svg>
  </div>
  <h3>Delivery</h3>
  <p>Your order is on its way. Expect<br>delivery within 10–15 business days.</p>
</div>

<!-- Footer -->
<footer class="abs footer">
  <div class="abs" style="left:150px;top:68px;width:40px;height:40px;border-radius:50%;background:var(--white)"></div>
  <div class="abs" style="left:110px;top:118px;font-family:'Playfair Display',serif;font-weight:700;font-size:36px">Brimwork</div>
  <div class="newsletter"><span>Enter email address</span><b>Send</b></div>
  <span class="social" style="left:123px;background:var(--orange)"></span>
  <span class="social" style="left:158px;background:var(--white)"></span>
  <span class="social" style="left:191px;background:var(--white)"></span>

  <h4 style="left:442px">Quick Links</h4>
  <ul class="flist" style="left:442px">
    <li>Home</li><li>Customization Hat</li><li>FAQ</li><li>Delivery timeline</li><li>Testimonials</li>
  </ul>
  <h4 style="left:653px">Help Links</h4>
  <ul class="flist" style="left:653px">
    <li>Terms &amp; Conditions</li><li>Privacy Policy</li><li>Shipping &amp; Returns</li><li>Cookie Preferences</li>
  </ul>
  <h4 style="left:868px">Contact Us</h4>
  <div class="contact" style="top:128px">
    <span class="ic"><svg width="11" height="11" viewBox="0 0 11 11"><path d="M2 1l2 0 1 3-1.5 1a6 6 0 0 0 2.5 2.5L7 6l3 1v2c-5 1-9-3-8-8z" fill="#fff"/></svg></span>+1 555 014 2290</div>
  <div class="contact" style="top:162px">
    <span class="ic"><svg width="11" height="9" viewBox="0 0 11 9"><rect x=".5" y=".5" width="10" height="8" fill="#fff"/><path d="M1 1l4.5 4L10 1" stroke="#ff6b22" fill="none"/></svg></span>hello@brimwork.com</div>
  <div class="contact" style="top:198px">
    <span class="ic"><svg width="9" height="12" viewBox="0 0 9 12"><path d="M4.5 12S0 7 0 4.5a4.5 4.5 0 0 1 9 0C9 7 4.5 12 4.5 12z" fill="#fff"/><circle cx="4.5" cy="4.5" r="1.6" fill="#ff6b22"/></svg></span>210 Harbor Lane,<br>Portland, OR 97201,</div>

  <div class="copy">©Copyrights 2025. All Rights Reserved.</div>
</footer>

</body>
</html>
```